Corvelle Strategies business card

I need a business card for my new strategic consulting LLC, Corvelle Strategies. We specialize in helping people who care about broadband technology and telecommunications policy, and we're based in Washington DC. I'm looking for a card that says smart, credible, future-facing and signals a high level of expertise. It's DC, so there's clearly a limit to how crazy we can go with this card, but I am looking for a design that reflects a company that is comfortable with technology, policy, and having a little bit fun. I'm uploading my logo below, and I'd like to have it be part of the card design in some fashion.
Target Market(s)
Telecommunications and technology policy professionals
Industry/Entity Type
Technology policy
Contact Information for Business Card
Name of business, my name (Glen Mosswater), email (glen@corvellestrategies-example.com) , phone number (202-555-0148)phone number

```html
<!DOCTYPE html>
<html lang="en">
<head>
<meta charset="utf-8">
<title>Corvelle Strategies – Business Card</title>
<link rel="stylesheet" href="https://fonts.googleapis.com/css2?family=Montserrat:wght@400;500;700;800&display=swap">
<style>
  :root {
    --page-bg: #e4e4e6;
    --navy: #2b4878;
    --navy-deep: #1e3564;
    --brand-blue: #2a4b8f;
    --gold: #f3b63f;
    --paper: #f3f3f2;
    --ink: #1f2f55;
    --white: #ffffff;
  }
  * { box-sizing: border-box; margin: 0; padding: 0; }
  html, body { width: 1200px; height: 936px; overflow: hidden; }
  body {
    background: var(--page-bg);
    font-family: "Montserrat", Arial, sans-serif;
    position: relative;
  }
  .card {
    position: absolute;
    left: 240px;
    width: 720px;
    height: 412px;
    border-radius: 28px;
    overflow: hidden;
    box-shadow: 0 10px 28px rgba(0,0,0,0.18);
  }

  /* Front */
  .card-front { top: 36px; background: var(--navy); }
  .tagline {
    position: absolute; left: 52px; top: 46px;
    list-style: none;
    color: var(--white);
    font-size: 21px; font-weight: 500;
    letter-spacing: 0.12em; line-height: 1.3;
    z-index: 2;
  }
  .tagline .accent { color: var(--gold); }
  .skyline-art {
    position: absolute; inset: 0;
    background:
      radial-gradient(ellipse 260px 70px at 300px 300px, rgba(243,182,63,0.28), transparent 100%),
      radial-gradient(ellipse 380px 110px at 320px 340px, rgba(80,140,240,0.42), transparent 100%),
      radial-gradient(ellipse 240px 80px at 560px 360px, rgba(70,130,230,0.30), transparent 100%),
      radial-gradient(ellipse 160px 150px at 240px 240px, rgba(150,175,220,0.12), transparent 100%);
  }
  .front-brand {
    position: absolute; right: 52px; bottom: 44px;
    display: flex; align-items: center; gap: 12px;
    color: var(--white);
    font-size: 30px; font-weight: 800;
    z-index: 2;
  }
  .brand-dot { width: 18px; height: 18px; border-radius: 50%; background: var(--gold); flex-shrink: 0; }

  /* Back */
  .card-back { top: 488px; background: var(--paper); }
  .corner-band {
    position: absolute; left: 0; bottom: 0;
    width: 720px; height: 412px;
  }
  .back-brand {
    position: absolute; left: 48px; top: 48px;
    display: flex; align-items: center; gap: 16px;
    color: var(--brand-blue);
    font-size: 50px; font-weight: 800;
    letter-spacing: -0.01em;
  }
  .back-brand .brand-dot { width: 26px; height: 26px; }
  .divider {
    position: absolute; left: 340px; top: 200px;
    width: 1.5px; height: 170px;
    background: var(--gold);
    opacity: 0.7;
  }
  .contact { position: absolute; left: 372px; top: 196px; color: var(--ink); }
  .contact-name { font-size: 20px; font-weight: 800; letter-spacing: 0.06em; }
  .contact-title { font-size: 13px; font-weight: 500; letter-spacing: 0.12em; margin-top: 4px; }
  .contact-list { list-style: none; margin-top: 20px; }
  .contact-list li {
    display: flex; align-items: center; gap: 12px;
    font-size: 14px; font-weight: 500;
    margin-bottom: 11px;
    white-space: nowrap;
  }
  .icon {
    width: 28px; height: 28px; border-radius: 50%;
    background: var(--ink);
    display: flex; align-items: center; justify-content: center;
    flex-shrink: 0;
  }
</style>
</head>
<body>

<section class="card card-front" aria-label="Card front">
  <div class="skyline-art" role="img" aria-label="Line drawing of the Washington DC skyline with flowing blue and gold light streaks"></div>
  <ul class="tagline">
    <li>CONNECTING</li>
    <li>TECHNOLOGY</li>
    <li>INFORMING POLICY</li>
    <li class="accent">ADVANCING IMPACT</li>
  </ul>
  <div class="front-brand">
    <span class="brand-name">Corvelle Strategies</span>
    <span class="brand-dot"></span>
  </div>
</section>

<section class="card card-back" aria-label="Card back">
  <svg class="corner-band" viewBox="0 0 720 412" aria-hidden="true">
    <polygon points="0,330 0,412 150,412" fill="var(--navy-deep)"/>
  </svg>
  <div class="back-brand">
    <span class="brand-name">Corvelle Strategies</span>
    <span class="brand-dot"></span>
  </div>
  <div class="divider"></div>
  <div class="contact">
    <p class="contact-name">GLEN MOSSWATER</p>
    <p class="contact-title">PRINCIPAL</p>
    <ul class="contact-list">
      <li>
        <span class="icon">
          <svg width="14" height="14" viewBox="0 0 16 16" fill="none" stroke="#f3b63f" stroke-width="1.6"><rect x="1.5" y="3.5" width="13" height="9" rx="1"/><path d="M1.5 4l6.5 5 6.5-5"/></svg>
        </span>
        glen@corvellestrategies-example.com
      </li>
      <li>
        <span class="icon">
          <svg width="14" height="14" viewBox="0 0 16 16" fill="#f3b63f"><path d="M4 1.5l2.2 2.8-1.3 1.6c.8 1.8 2.4 3.4 4.2 4.2l1.6-1.3 2.8 2.2-1.2 2.2c-5.4-.4-9.6-4.6-10-10z"/></svg>
        </span>
        202-555-0148
      </li>
      <li>
        <span class="icon">
          <svg width="14" height="14" viewBox="0 0 16 16" fill="#f3b63f"><path d="M8 1a5 5 0 0 0-5 5c0 3.8 5 9 5 9s5-5.2 5-9a5 5 0 0 0-5-5zm0 7a2 2 0 1 1 0-4 2 2 0 0 1 0 4z"/></svg>
        </span>
        Washington, DC
      </li>
    </ul>
  </div>
</section>

</body>
</html>
```